Fresh Website for PLUM and Kuvo alliance

Page designs for 11 pages using existing Jigsaw template for the homepage and existing company logo.

Mock-up of front page attached, feel free to turn it into something elegant, professional and clean.

Target Market(s)

1. Small to medium business owners who use QELN or other accounting software who want to use Kuvo.
2 Businesses who want to hire a decent Bookkeeper instead of trying to do it on the kitchen table at night.

Industry/Entity Type

It Company

Font styles to use
Sans Serif

Colors
86cae6
32a6d6
34a7d8
cee9f5

Requirements
Must have
• Use the Kuvo blue colour for the website theme - PMS: Blue #00A0C6
Use the Jigsaw template design and theme - pieces of the puzzle all fitting together with Kuvo and PLUM
Same font used in the plum blue png uploaded and plumtraining logo
Nice to have
• A style that mirrors and links easily with the Kuvo website:
check out www.kuvoledger.com.au
Should not have
• Cheesy pictures of money and $$,
Cluttered feel
Chunky anime like images for buttons icons
Not to scream Jigsaw and make everything look like a kids website - just subtle nods to the theme

```html
<!DOCTYPE html>
<html lang="en">
<head>
<meta charset="utf-8">
<title>PLUM Training – About Us</title>
<link rel="stylesheet" href="https://fonts.googleapis.com/css2?family=Questrial&display=swap">
<style>
  :root {
    --brand-blue: #32a6d6;
    --brand-blue-deep: #1c94c6;
    --sky-light: #cee9f5;
    --sky-mid: #86cae6;
    --ink: #1a1a1a;
    --ink-soft: #333333;
    --rule: #d9d9d9;
    --panel-grey: #ececec;
    --page-bg: #ffffff;
  }
  * { box-sizing: border-box; margin: 0; padding: 0; }
  html, body {
    width: 1200px;
    height: 850px;
    overflow: hidden;
    background: var(--page-bg);
    font-family: "Questrial", "Century Gothic", sans-serif;
    color: var(--ink);
  }
  .site {
    position: relative;
    width: 1200px;
    height: 850px;
  }

  /* Header */
  .site-header {
    height: 100px;
    background: linear-gradient(#ffffff 0%, #ffffff 88%, #f2f2f2 100%);
    border-bottom: 2px solid var(--rule);
    position: relative;
  }
  .brand {
    position: absolute;
    left: 193px;
    top: 24px;
    display: flex;
    align-items: center;
    gap: 10px;
    color: var(--brand-blue);
    font-size: 34px;
    letter-spacing: 0.5px;
    line-height: 1;
  }
  .brand-square {
    width: 44px;
    height: 44px;
    background: var(--brand-blue);
  }
  .main-nav {
    position: absolute;
    right: 204px;
    top: 36px;
    display: flex;
    gap: 6px;
    align-items: center;
  }
  .main-nav a {
    display: block;
    padding: 5px 9px;
    font-size: 14px;
    color: var(--ink);
    text-decoration: none;
    font-weight: 600;
  }
  .main-nav a.is-active {
    background: var(--brand-blue);
    color: #fff;
  }

  /* Content panel */
  .content-panel {
    position: absolute;
    left: 180px;
    top: 132px;
    width: 816px;
    height: 560px;
    border: 1px solid var(--rule);
    display: flex;
    background: #fff;
  }
  .side-nav {
    width: 160px;
    background: linear-gradient(#e4e4e4, #f7f7f7 70%, #ffffff);
    padding-top: 36px;
  }
  .side-nav a {
    display: block;
    padding: 9px 22px;
    font-size: 14px;
    color: var(--brand-blue);
    text-decoration: none;
  }
  .side-nav a.is-current {
    background: #fff;
    color: var(--ink);
  }
  .page-body {
    flex: 1;
    padding: 14px 18px 0 36px;
  }
  .page-title {
    font-size: 22px;
    font-weight: 400;
    color: var(--ink);
    margin-bottom: 12px;
  }
  .team-banner {
    width: 600px;
    height: 130px;
    border: 1px solid var(--rule);
    padding: 6px;
    margin-bottom: 12px;
  }
  .team-banner-fill {
    width: 100%;
    height: 100%;
    background: linear-gradient(180deg, var(--sky-light) 0%, var(--sky-mid) 55%, #3c4a55 100%);
  }
  .page-body p {
    font-size: 12.5px;
    line-height: 1.38;
    color: var(--ink-soft);
    margin-bottom: 12px;
    max-width: 600px;
  }
  .page-body p.closing-line {
    font-weight: 700;
    color: var(--ink);
  }
</style>
</head>
<body>
<div class="site">
  <header class="site-header">
    <div class="brand">
      <span class="brand-square"></span>
      <span class="brand-name">PLUM Training</span>
    </div>
    <nav class="main-nav">
      <a href="#">Home</a>
      <a href="#" class="is-active">About</a>
      <a href="#">Learn More</a>
      <a href="#">Initial Consult</a>
      <a href="#">Clients</a>
      <a href="#">Contact</a>
      <a href="#">Blog</a>
    </nav>
  </header>

  <section class="content-panel">
    <nav class="side-nav">
      <a href="#" class="is-current">About Us</a>
      <a href="#">our Team</a>
      <a href="#">Career</a>
    </nav>
    <article class="page-body">
      <h1 class="page-title">About Us</h1>
      <div class="team-banner">
        <div class="team-banner-fill" role="img" aria-label="Silhouettes of business people standing in a row against a light blue office backdrop"></div>
      </div>
      <p>Every business, from sole trader to multi-national, has hopes and dreams – they also have families and communities behind them. PLUM is part of your extended family, committed to providing you with the support and guidance to make your business goals a reality.</p>
      <p>PLUM gets you started, helps you develop and delivers solutions as you grow.<br>With 20 years experience, we provide a range of comprehensive services from Kuvo setup, training, bookkeeping and ongoing support.</p>
      <p>More than just Bookkeepers!</p>
      <p>PLUM started out as Halvern Pike &amp; Associates in 1997 with Marla Pike providing quality bookkeeping services to small businesses in the Sydney Metro area.</p>
      <p>Following repeated requests for Marla to "clone" herself, Marla embarked on the task of finding other professionals who were as passionate about bookkeeping and exceptional service.</p>
      <p>As the business grew, requests for expanded services created the need for a namechange, thus Plum Ledger Services Pty Ltd evolved.</p>
      <p>PLUM is now a team of professionals all contributing unique skills and experience to the group.</p>
      <p class="closing-line">And yes, we still have the first client we started with in 1997!</p>
    </article>
  </section>
</div>
</body>
</html>
```